Web Design Project for Lumen Harbor

Design a new web site for Lumen Harbor.

Current design - www.lumenharbor.example
Latest design - store.lumenharbor.example

Close site we like - www.qvr.example

The new design has to be welcoming, fresh, non-industrial, light, friendly and functional.

Target Market(s)

Enterprise IT professionals. In particular, CIO's and IT Managers.

Industry/Entity Type

Store

Requirements
Must have
• Same functionality as the new design.
Should not have
• We want to be able to target different users with different content..... it somethings important to CIO's and not important to Service Delivery Managers, which is different from Network Managers, and different from CFO's.

```html
<!DOCTYPE html>
<html lang="en">
<head>
<meta charset="utf-8">
<title>Lumen Harbor</title>
<link href="https://fonts.googleapis.com/css2?family=Arimo:wght@400;700&display=swap" rel="stylesheet">
<style>
:root{
  --blue:#1a5f9e;
  --blue-dark:#14507f;
  --blue-light:#a9c3da;
  --green:#22a14a;
  --text:#555;
  --panel:#eeeeee;
}
*{margin:0;padding:0;box-sizing:border-box}
html,body{width:800px;height:1200px;overflow:hidden;background:#fff}
body{position:relative;font-family:'Arimo',Arial,sans-serif;color:var(--text)}
.abs{position:absolute}
.header-curve{left:0;top:0}
.brand{left:98px;top:56px}
.brand-name{font-size:23px;font-weight:700;color:var(--blue);letter-spacing:-.2px}
.brand-tag{left:146px;top:84px;font-size:8px;font-weight:700;color:var(--green)}
.login{left:451px;top:64px;font-size:10px;font-weight:700;color:var(--blue);display:flex;align-items:center;gap:5px;letter-spacing:.3px}
.login i{width:13px;height:13px;background:var(--green);display:block;border-radius:2px}
.hero{left:140px;top:140px;width:520px;height:270px;background:radial-gradient(ellipse at 60% 45%,#cfc9c2 0%,#e9e6e2 45%,#fff 75%)}
.nav{left:65px;top:395px;width:495px;height:72px;background:linear-gradient(#4b86bb,var(--blue-dark));border-radius:0 0 8px 8px;display:flex;align-items:flex-end;padding-left:8px}
.nav a{color:#fff;text-decoration:none;font-size:13px;padding:0 7px 12px;height:54px;display:flex;align-items:flex-end;border-right:1px solid rgba(255,255,255,.25)}
.nav a:last-child{border-right:0}
.section-title{font-size:17px;font-weight:400;color:var(--blue);border-bottom:2px solid #d6d6d6;padding-bottom:6px}
.section-title span{color:#555}
.section-title small{font-size:12px;color:#444;font-weight:400}
.intro-title{left:66px;top:500px;width:494px}
.tablet{left:66px;top:545px;width:66px;height:60px;background:linear-gradient(135deg,#555,#1b1b1b);border-radius:4px}
.intro-text{left:139px;top:539px;width:418px;font-size:10.5px;line-height:15.2px;letter-spacing:.9px;text-align:justify;color:#555}
.more{width:54px;height:18px;background:var(--green);color:#fff;font-size:9px;letter-spacing:.5px;border-radius:2px;display:flex;align-items:center;justify-content:center;gap:4px}
.more::before{content:"";border-left:5px solid #fff;border-top:3px solid transparent;border-bottom:3px solid transparent}
.solutions-title{left:66px;top:676px;width:494px}
.solution-list{left:78px;top:715px;list-style:none;font-size:10px;color:#444;letter-spacing:.2px}
.solution-list li{height:18.7px;display:flex;align-items:center;gap:8px}
.solution-list li::before{content:"";width:11px;height:11px;border-radius:50%;background:var(--green);flex:none}
.figure{left:430px;top:740px;width:100px;height:130px;background:radial-gradient(ellipse at 50% 45%,#bdbdbd,#eee 65%,#fff 80%)}
.news-title{left:578px;top:503px;width:194px;padding-left:3px;color:var(--green)}
.news{left:578px;width:194px;font-size:10px;line-height:15.2px;letter-spacing:.45px;color:#555;text-align:justify}
.news .read{text-align:right;font-weight:700;color:#777}
.news .read u{color:#666}
.panel{left:64px;top:935px;width:708px;height:210px;background:linear-gradient(#e4e4e4,#f7f7f7 40%,#fff);border-radius:6px 6px 0 0}
.feature{width:210px;font-size:8.4px;line-height:10px;color:var(--blue);letter-spacing:.2px;text-align:justify}
.feature h3{font-size:9.5px;color:#555;margin-bottom:6px;letter-spacing:.5px}
.feature .lm{float:right}
.icon{width:34px;height:26px;background:linear-gradient(#6f9cc8,#1d4f86);border:2px solid #c8d6e4;border-radius:2px}
.advanced{left:83px;top:1072px;width:370px;font-size:9.6px;color:var(--blue);letter-spacing:.5px;line-height:12px}
.advanced h3{font-size:13px;font-weight:400;color:var(--blue);text-decoration:underline;margin-bottom:4px}
.advanced h3 span{color:#444}
.footer-wave{left:0;top:1110px}
.copyright{left:64px;top:1174px;font-size:8.5px;color:#fff;letter-spacing:.4px}
.copyright b{color:#b9e3c4;font-weight:400}
.footer-links{right:31px;top:1174px;font-size:8.5px;color:#fff;letter-spacing:.4px;display:flex;gap:10px}
.footer-links a{color:#fff;text-decoration:none}
.footer-links a:first-child{text-decoration:underline}
</style>
</head>
<body>
<svg class="abs header-curve" width="800" height="160" viewBox="0 0 800 160" aria-hidden="true">
  <path d="M0 0H800V25C620 55 420 140 230 120C120 110 40 95 0 88Z" fill="#f1f1f1"/>
  <path d="M0 88C40 95 120 110 230 120C420 140 620 55 800 25" fill="none" stroke="var(--blue-light)" stroke-width="4"/>
</svg>

<div class="abs brand"><span class="brand-name">Lumen Harbor</span></div>
<div class="abs brand-tag">Next Generation Monitoring Solutions</div>
<div class="abs login"><i></i>Register/ Login</div>

<div class="abs hero" role="img" aria-label="Photograph of a smiling businessman in front of a group of colleagues"></div>

<svg class="abs" style="left:0;top:385px" width="800" height="50" viewBox="0 0 800 50" aria-hidden="true">
  <path d="M0 22C120 0 260 0 400 15C560 32 700 35 800 28" fill="none" stroke="var(--blue-light)" stroke-width="4"/>
</svg>

<nav class="abs nav">
  <a href="#">Home</a><a href="#">Solutions</a><a href="#">Technology</a><a href="#">Resources</a><a href="#">Partners</a><a href="#">Company</a><a href="#">Support</a>
</nav>

<h2 class="abs section-title intro-title">Industry Leading - <small>helping organisations discover the power of events</small></h2>
<div class="abs tablet" role="img" aria-label="Tablet computer showing a dashboard"></div>
<p class="abs intro-text">The Cedar Hollow Event Hall is looking for a website design. We specialize in all types of events from weddings to company outings. We have an amazing rustic barn to fit any service and can also provide a complete multi-unit home that includes.<br>10 bedrooms (sleeps 20 comfortably), 5 full bathis a professional chef style and 1 full professional outdoor kitchen. The Cedar Hollow Event Hall is looking for a website design. We specialize in all types of events from weddings to company outings.</p>
<div class="abs more" style="left:503px;top:660px">More</div>

<h2 class="abs section-title solutions-title">Lumen Harbor <span>Solutions</span></h2>
<ul class="abs solution-list">
  <li>Large Scale Vehicle Tracking with ANPR</li>
  <li>Real Time Asset Condition Monitoring</li>
  <li>Customer Experience Monitoring</li>
  <li>Environmental Monitoring</li>
  <li>Event Driven Application Platform</li>
  <li>Information and Communications Technology Monitoring</li>
  <li>PC Power Management for Workstation Fleets</li>
  <li>Product Lifecycle Management</li>
  <li>Security and Surveillance</li>
  <li>Traffic and Transport Systems</li>
  <li>Utility Network Management</li>
</ul>
<div class="abs figure" role="img" aria-label="3D figure holding a large wrench"></div>
<div class="abs more" style="left:502px;top:908px">More</div>

<h2 class="abs section-title news-title">Latest <span>News</span></h2>
<div class="abs news" style="top:538px"><p>Lumen Harbor is proud to announce that it is the Gold Sponsor of the Northgate CIO Summit 2010</p><p>Wednesday, April 7, 2010</p><p class="read"><u>Read More</u> &gt;&gt;</p></div>
<div class="abs news" style="top:642px"><p>Lumen Harbor is proud to announce that it is the Gold Sponsor of the Northgate CIO Summit 2010</p><p>Wednesday, April 7, 2010</p><p class="read"><u>Read More</u> &gt;&gt;</p></div>
<div class="abs news" style="top:745px"><p>Lumen Harbor is proud to announce that it is the Gold Sponsor of the Northgate CIO Summit 2010</p><p>Wednesday, April 7, 2010</p><p class="read"><u>Read More</u> &gt;&gt;</p></div>
<div class="abs news" style="top:848px"><p>Lumen Harbor is proud to announce that it is the Gold Sponsor of the Northgate CIO Summit 2010</p><p>Wednesday, April 7, 2010</p><p class="read"><u>Read More</u> &gt;&gt;</p></div>

<div class="abs panel"></div>
<div class="abs icon" style="left:86px;top:951px"></div>
<div class="abs icon" style="left:316px;top:951px"></div>
<div class="abs icon" style="left:544px;top:951px"></div>
<div class="abs icon" style="left:488px;top:1059px"></div>

<div class="abs feature" style="left:83px;top:983px"><h3>Lumen Harbor EPN</h3>Lumen Harbor can help you solve real world business problems with complex event processing. Gain an understanding of how Lumen Harbor and event processing can help your business. <span class="lm">» Learn More</span></div>
<div class="abs feature" style="left:313px;top:983px"><h3>Desktop Energy Management</h3>Voltwise delivers real-time visibility to PC workstation fleet owners and operators of energy consumption patterns, costs, and CO2 emissions associated with day-to-day corporate operations. <span class="lm">» Learn More</span></div>
<div class="abs feature" style="left:541px;top:983px"><h3>Lumen Harbor Last Mile Advantage</h3>Acquiring event data in environments with heterogeneous devices and or geographic distribution is tedious and time consuming. See how Lumen Harbor can help you tackle this task with ease. <span class="lm">» Learn More</span></div>
<div class="abs feature" style="left:541px;top:1056px"><h3>Event Driven Application Platform</h3>Lumen Harbor provides an industry leading enterprise class platform for the rapid development and deployment of event driven applications. <span class="lm">» Learn More</span></div>

<div class="abs advanced"><h3>Advanced <span>Technology Program</span></h3>Lumen Harbor offers advanced previews to select customers and industry insiders. To see if you qualify. <span style="float:right;margin-right:12px">» Learn More</span></div>

<svg class="abs footer-wave" width="800" height="90" viewBox="0 0 800 90" aria-hidden="true">
  <defs><linearGradient id="footerFill" x1="0" y1="0" x2="0" y2="1"><stop offset="0" stop-color="#3f7fb6"/><stop offset="1" stop-color="#1a5b93"/></linearGradient></defs>
  <path d="M0 40C150 15 300 20 420 35C560 50 700 30 800 15V90H0Z" fill="url(#footerFill)"/>
  <path d="M0 40C150 15 300 20 420 35C560 50 700 30 800 15" fill="none" stroke="#b8cfe3" stroke-width="3"/>
</svg>
<div class="abs copyright">Copyright @ 2012, <b>Lumen Harbor</b></div>
<div class="abs footer-links"><a href="#">Home</a>|<a href="#">Solutions</a>|<a href="#">Technology</a>|<a href="#">Resources</a>|<a href="#">Partners</a>|<a href="#">Company</a>|<a href="#">Support</a></div>
</body>
</html>
```